help me Create Brightfern Catering offsite menus

I need something vibrant and it needs some pictures to go with the food i will include the logo of the location and the menu. it is for offsite catering to be delivered to venues in our local town, we are currently catering in house only but are expanding to do delivery so need something that i can use as a menu. the file needs to be able to be edited

Target Market(s)

local small businesses that require catering for their group lunches

Industry/Entity Type

Catering

Font styles to use
Serif
Decorative

Requirements
Must have
• colour and soul, must have a good feeling and be happy
Nice to have
• some other stock photos of the described products
Should not have
• not be too corporate and businessy

```html
<!DOCTYPE html>
<html lang="en">
<head>
<meta charset="utf-8">
<title>Brightfern Catering – Conference Menu</title>
<link href="https://fonts.googleapis.com/css2?family=Lato:ital,wght@0,300;0,400;0,700;1,300&display=swap" rel="stylesheet">
<style>
  :root {
    --ink: #2a2a33;
    --muted: #4f4f58;
    --rule: #c9c9cf;
    --navy: #2c2a3f;
    --pink: #c4346e;
    --orange: #ef9a2a;
    --green: #8cb63c;
    --paper: #ffffff;
  }
  * { margin: 0; padding: 0; box-sizing: border-box; }
  html, body { width: 845px; height: 1200px; overflow: hidden; background: var(--paper); }
  body { font-family: "Lato", sans-serif; color: var(--ink); position: relative; }

  .booking-line {
    position: absolute; top: 22px; left: 0; width: 100%;
    text-align: center; font-size: 18px; font-weight: 300; color: var(--ink);
    white-space: nowrap;
  }
  .booking-line strong { font-weight: 700; }

  .food-banner {
    position: absolute; top: 50px; left: 0; width: 845px; height: 353px;
    background: linear-gradient(90deg, #a8603c 0%, #d9a277 22%, #efe2cf 45%, #f3e9da 55%, #d8a25e 75%, #b77839 100%);
  }

  .brand-mark { position: absolute; top: 50px; left: 0; width: 845px; height: 353px; }

  .brand-name {
    position: absolute; top: 212px; left: 0; width: 845px; text-align: center;
    font-weight: 700; font-size: 44px; line-height: 56px; color: #fff;
  }

  .menu-title {
    position: absolute; top: 430px; left: 0; width: 100%;
    text-align: center; font-size: 38px; line-height: 52px; font-weight: 300; color: var(--ink);
    white-space: nowrap;
  }
  .menu-title .dot { display: inline-block; width: 11px; height: 11px; border-radius: 50%; margin: 0 6px; vertical-align: middle; }
  .dot.pink { background: var(--pink); }
  .dot.orange { background: var(--orange); }
  .dot.green { background: var(--green); }
  .menu-title .label { margin: 0 14px; }

  .menu { position: absolute; top: 522px; left: 56px; width: 739px; }
  .menu-section { margin-bottom: 20px; }
  .section-heading {
    font-size: 22px; line-height: 32px; font-weight: 700; color: var(--ink);
    padding-bottom: 6px; border-bottom: 1.5px solid var(--rule);
  }
  .menu-item {
    display: flex; align-items: center; height: 39px;
    font-size: 19px; font-weight: 300; color: var(--muted); white-space: nowrap;
  }
  .menu-section.tea .menu-item { height: 38.5px; }
  .menu-item .name { width: 564px; overflow: hidden; }
  .menu-item .price { font-style: italic; }
</style>
</head>
<body>
  <p class="booking-line">To book in your event call us Now on 55 010 482 or go to <strong>www.brightferndining.com.au</strong></p>

  <div class="food-banner" role="img" aria-label="Catering spread of cured meats, cheeses, fresh bread, muffins and pastries"></div>

  <svg class="brand-mark" viewBox="0 0 845 353" aria-hidden="true">
    <circle cx="422" cy="190" r="140" fill="var(--navy)"/>
  </svg>
  <div class="brand-name">Brightfern</div>

  <h1 class="menu-title">
    <span class="dot pink"></span><span class="dot orange"></span><span class="dot green"></span><span class="label">conference menu</span><span class="dot pink"></span><span class="dot orange"></span><span class="dot green"></span>
  </h1>

  <main class="menu">
    <section class="menu-section">
      <h2 class="section-heading">TEA &amp; COFFEE</h2>
      <div class="menu-item"><span class="name">Tea and coffee station</span><span class="price">$3.00 pp</span></div>
      <div class="menu-item"><span class="name">Continuous tea and coffee enough to serve for the day</span><span class="price">$5.00 pp</span></div>
      <div class="menu-item"><span class="name">Barrista delivered (pre order only)</span><span class="price">$5.50 each</span></div>
    </section>
    <section class="menu-section">
      <h2 class="section-heading">EXTRAS</h2>
      <div class="menu-item"><span class="name">Juice 2 Lt Bottle</span><span class="price">$3.95</span></div>
    </section>
    <section class="menu-section tea">
      <h2 class="section-heading">Morning or afternoon Tea</h2>
      <div class="menu-item"><span class="name">Scones and slices platter</span><span class="price">$6.50 per person</span></div>
      <div class="menu-item"><span class="name">Muffins</span><span class="price">$5.00 per person</span></div>
      <div class="menu-item"><span class="name">Homemade biscuits</span><span class="price">$4.50 per person</span></div>
      <div class="menu-item"><span class="name">Banana Bread</span><span class="price">$6.00 per person</span></div>
      <div class="menu-item"><span class="name">Gluten Free frittata</span><span class="price">$5.50 per person</span></div>
      <div class="menu-item"><span class="name">Ploughmans Platter</span><span class="price">$8.50 per person</span></div>
      <div class="menu-item"><span class="name">Whole fresh fruit platter</span><span class="price">$45.00 per platter</span></div>
      <div class="menu-item"><span class="name">Chopped fresh seasonal fruit Platter</span><span class="price">$49.50 per platter</span></div>
    </section>
  </main>
</body>
</html>
```